Business card design for Bront Engineering Qavo

We need a new business card design along with all the necessary to place an order. The company is Bront Engineering Qavo and we recently updated our logo.

```html
<!DOCTYPE html>
<html lang="en">
<head>
<meta charset="utf-8">
<title>Bront Engineering Qavo – Business Card</title>
<link href="https://fonts.googleapis.com/css2?family=Poppins:wght@400;500;600;700&display=swap" rel="stylesheet">
<style>
  :root {
    --page: #ffffff;
    --card-front: #939392;
    --card-back: #ffffff;
    --brand-grey: #939392;
    --brand-yellow: #e2bd2a;
    --text-grey: #6f6f6f;
    --rule: #8a8a8a;
    --shadow: rgba(0, 0, 0, 0.28);
  }
  * { box-sizing: border-box; margin: 0; padding: 0; }
  html, body {
    width: 979px;
    height: 1200px;
    overflow: hidden;
    background: var(--page);
    font-family: "Poppins", Arial, sans-serif;
  }
  .canvas {
    position: relative;
    width: 979px;
    height: 1200px;
  }
  .card {
    position: absolute;
    left: 119px;
    width: 745px;
    height: 426px;
    box-shadow: 8px 10px 14px var(--shadow);
  }
  .card--front { top: 140px; background: var(--card-front); }
  .card--back  { top: 648px; background: var(--card-back); }

  .wordmark {
    position: absolute;
    display: flex;
    align-items: center;
    gap: 14px;
    font-weight: 600;
    letter-spacing: 0.04em;
    text-transform: uppercase;
    white-space: nowrap;
  }
  .wordmark__square {
    width: 30px;
    height: 30px;
    flex: none;
  }
  .card--front .wordmark {
    left: 0; right: 0; top: 190px;
    justify-content: center;
    font-size: 36px;
    color: #ffffff;
  }
  .card--front .wordmark__square { background: #ffffff; }

  .card--back .wordmark {
    left: 34px; top: 100px;
    font-size: 30px;
    color: var(--brand-grey);
  }
  .card--back .wordmark__square { background: var(--brand-yellow); width: 26px; height: 26px; }

  .person {
    position: absolute;
    left: 46px;
    top: 254px;
  }
  .person__name {
    font-size: 25px;
    font-weight: 700;
    color: var(--brand-yellow);
    line-height: 1.1;
  }
  .person__role {
    font-size: 16px;
    color: var(--text-grey);
    line-height: 1.3;
  }
  .divider {
    position: absolute;
    left: 46px;
    top: 314px;
    width: 650px;
    height: 2px;
    background: var(--rule);
  }
  .contacts {
    position: absolute;
    left: 52px;
    top: 328px;
    list-style: none;
  }
  .contacts li {
    display: flex;
    align-items: center;
    gap: 14px;
    height: 27px;
    font-size: 18px;
    color: var(--text-grey);
  }
  .contacts svg { width: 18px; height: 18px; flex: none; fill: var(--brand-yellow); }
  .address {
    position: absolute;
    right: 41px;
    top: 355px;
    text-align: right;
    font-size: 18px;
    line-height: 27px;
    color: var(--text-grey);
  }
</style>
</head>
<body>
<main class="canvas">
  <section class="card card--front" aria-label="Card front">
    <div class="wordmark">
      <span class="wordmark__square"></span>
      <span>Bront Engineering Qavo</span>
    </div>
  </section>

  <section class="card card--back" aria-label="Card back">
    <div class="wordmark">
      <span class="wordmark__square"></span>
      <span>Bront Engineering Qavo</span>
    </div>

    <div class="person">
      <p class="person__name">Name Name</p>
      <p class="person__role">CEO</p>
    </div>

    <div class="divider"></div>

    <ul class="contacts">
      <li>
        <svg viewBox="0 0 24 24" aria-hidden="true"><path d="M6.6 10.8a15.1 15.1 0 0 0 6.6 6.6l2.2-2.2a1 1 0 0 1 1-.25 11.4 11.4 0 0 0 3.6.57 1 1 0 0 1 1 1V20a1 1 0 0 1-1 1A17 17 0 0 1 3 4a1 1 0 0 1 1-1h3.5a1 1 0 0 1 1 1c0 1.25.2 2.45.57 3.6a1 1 0 0 1-.25 1z"/></svg>
        <span>000-000-0000</span>
      </li>
      <li>
        <svg viewBox="0 0 24 24" aria-hidden="true"><path d="M2 5h20v2l-10 6L2 7z"/><path d="M2 9l10 6 10-6v10H2z"/></svg>
        <span>info@bront-qavo.com</span>
      </li>
      <li>
        <svg viewBox="0 0 24 24" aria-hidden="true"><path d="M12 2a10 10 0 1 0 0 20 10 10 0 0 0 0-20zm6.9 6h-3a15.6 15.6 0 0 0-1.4-3.9A8 8 0 0 1 18.9 8zM12 4c.8 1.2 1.5 2.5 1.9 4h-3.8c.4-1.5 1.1-2.8 1.9-4zM4.3 14a8.2 8.2 0 0 1 0-4h3.4a16.5 16.5 0 0 0 0 4zm.8 2h3a15.6 15.6 0 0 0 1.4 3.9A8 8 0 0 1 5.1 16zm3-8h-3a8 8 0 0 1 4.4-3.9A15.6 15.6 0 0 0 8.1 8zM12 20c-.8-1.2-1.5-2.5-1.9-4h3.8c-.4 1.5-1.1 2.8-1.9 4zm2.3-6H9.7a14.7 14.7 0 0 1 0-4h4.6a14.7 14.7 0 0 1 0 4zm.2 5.9a15.6 15.6 0 0 0 1.4-3.9h3a8 8 0 0 1-4.4 3.9zm1.8-5.9a16.5 16.5 0 0 0 0-4h3.4a8.2 8.2 0 0 1 0 4z"/></svg>
        <span>bront-qavo.com</span>
      </li>
    </ul>

    <p class="address">3361 Address Street, City,<br>Country Zip code</p>
  </section>
</main>
</body>
</html>
```